Venbrisk Card

We want a business card that shows people who we are the log attached was designed by the designers on graft hive,we are using the OO in the logo (speech bubbles as our icon,so please make that part of the card ) keep the colouring the same as the logo design and we will be using high end production on the card using silver foil as the icon to make it stand out.
As Venbrisk we specialise in finding influencers through social networks for brands, so if you used yammo to comment about sports products and you were followed by of lot of users and interacted with those users then the algorithm finds you and we contact you to work for our clients as a company we then have a set of influencers that we use to support new sports products.
Also we use our algorithm to help athletes,models etc to be scored via there digital influence so when say Orvel QD ask me to find a skater that is not so much a podium rider but is more digital focused for a digital campaign then we work out who those guys or girls are to help Orvel QD
Venbrisk is the name of the product and company, However I just wanted to give you the rationale of why we chose venbrisk in the first place. Aldo itself is an 'abbreviation' from the proper name Aldemar Fusk from Keeper of the Vales. The character was able to look into the morvendal (sometimes translated as "Seeing Stone" but literally meaning "Farsighted" or "One that Sees from Afar") and see into the far corners of the Universe. Much in the same way as the platform has been developed is able to look into the far corners of the social network arena to help brands and Athletes will be able to see how they rated....but don't worry i don't go running around in the woods with a foam Axe and an army of dwarfs!!!
Digital Directors,Brand Directors,Athletes,Models,Celebrities and agents
Business

```html
<!DOCTYPE html>
<html lang="en">
<head>
<meta charset="utf-8">
<title>Venbrisk Card</title>
<link href="https://fonts.googleapis.com/css2?family=Open+Sans:wght@400;600;700&display=swap" rel="stylesheet">
<style>
  :root {
    --backdrop: #2b2b2b;
    --card: #222222;
    --brand-blue: #4db2e4;
    --foil-silver: #b9b9b9;
    --text-light: #d0d0d0;
    --text-muted: #a8a8a8;
  }
  * { margin: 0; padding: 0; box-sizing: border-box; }
  html, body {
    width: 1200px;
    height: 900px;
    overflow: hidden;
    background: var(--backdrop);
    font-family: "Open Sans", Arial, sans-serif;
  }
  .stage {
    width: 1200px;
    height: 900px;
    display: flex;
    align-items: center;
    justify-content: center;
    gap: 44px;
  }
  .card {
    position: relative;
    width: 520px;
    height: 318px;
    background: var(--card);
    border-radius: 3px;
    box-shadow: 0 10px 30px rgba(0,0,0,0.35);
  }
  .wordmark {
    display: flex;
    align-items: center;
    gap: 10px;
    color: var(--brand-blue);
    font-weight: 700;
    letter-spacing: -1px;
    line-height: 1;
  }
  .wordmark-dot {
    flex: none;
    border-radius: 50%;
    background: var(--foil-silver);
  }

  /* Back: contact side */
  .card-back .holder {
    position: absolute;
    top: 34px;
    left: 150px;
  }
  .holder-name {
    color: var(--text-light);
    font-size: 19px;
    font-weight: 400;
  }
  .holder-role {
    color: var(--text-muted);
    font-size: 10px;
    letter-spacing: 0.5px;
    margin-top: 2px;
  }
  .card-back .wordmark {
    position: absolute;
    left: 36px;
    bottom: 62px;
    font-size: 46px;
  }
  .card-back .wordmark-dot { width: 22px; height: 22px; }
  .contact {
    position: absolute;
    top: 112px;
    left: 300px;
    list-style: none;
    color: var(--text-light);
    font-size: 13px;
    line-height: 18px;
  }
  .contact-label {
    display: inline-block;
    width: 16px;
    color: var(--brand-blue);
  }
  .contact-web {
    color: var(--brand-blue);
    font-weight: 700;
    margin-top: 4px;
  }

  /* Front: brand side */
  .card-front {
    display: flex;
    flex-direction: column;
    align-items: center;
    justify-content: center;
  }
  .card-front .wordmark { font-size: 78px; margin-top: 10px; }
  .card-front .wordmark-dot { width: 34px; height: 34px; }
  .front-web {
    margin-top: 34px;
    color: var(--brand-blue);
    font-size: 16px;
    font-weight: 700;
    letter-spacing: 1.5px;
  }
</style>
</head>
<body>
  <main class="stage">
    <section class="card card-back" aria-label="Card back">
      <div class="holder">
        <p class="holder-name">Daniel Corrow</p>
        <p class="holder-role">MARKETING DIRECTOR</p>
      </div>
      <ul class="contact">
        <li><span class="contact-label">T</span>0412 555 018</li>
        <li><span class="contact-label">M</span>03 9555 0142</li>
        <li><span class="contact-label">E</span>dcorrow@venbrisk.com</li>
        <li>Level 3, 18 Marlow St</li>
        <li>West Harbour NSW 2000</li>
        <li class="contact-web">www.venbrisk.com</li>
      </ul>
      <div class="wordmark"><span>venbrisk</span><span class="wordmark-dot"></span></div>
    </section>

    <section class="card card-front" aria-label="Card front">
      <div class="wordmark"><span>venbrisk</span><span class="wordmark-dot"></span></div>
      <p class="front-web">www.venbrisk.com</p>
    </section>
  </main>
</body>
</html>
```